Ward Compass Business Card Design*

We need a business card design for our company Ward Compass. Our company is specialized in providing online consulting services regarding medical institutions, hospitals and doctors. We work with patients worldwide looking to choose between healthcare providers. We have a website you may use as a reference, where we list doctors and clinics worldwide. So we target Medical providers as well as patients worldwide.
Target Market(s)
Medical Providers and patients around the world
Industry/Entity Type
Medical
Contact Information for Business Card
Salma Derkaoui
CEO
+90 612 348 2071
info@wardcompass-example.com
www.wardcompass-example.com
14 Annakhil 3 H.R.B. Rabat, Morocco
Requirements
Must have
- Company logo/name on one full side, personal info and smaller logo and company name on the other side.
Nice to have
- Smart and elegant design

```html
<!DOCTYPE html>
<html lang="en">
<head>
<meta charset="utf-8">
<title>Ward Compass Business Card</title>
<link rel="stylesheet" href="https://fonts.googleapis.com/css2?family=Roboto:wght@400;500;700&display=swap">
<style>
  :root {
    --navy: #1d2a7a;
    --white: #ffffff;
    --backdrop: #eef0f1;
  }
  * { box-sizing: border-box; margin: 0; padding: 0; }
  html, body { width: 1200px; height: 1198px; overflow: hidden; }
  body {
    position: relative;
    background: var(--backdrop);
    font-family: "Roboto", Arial, sans-serif;
  }
  .card {
    position: absolute;
    left: 185px;
    width: 826px;
  }
  .card-front {
    top: 90px;
    height: 493px;
    background: var(--white);
    display: flex;
    align-items: center;
    justify-content: center;
  }
  .card-back {
    top: 645px;
    height: 473px;
    background: var(--navy);
    color: var(--white);
  }
  .brand {
    display: flex;
    align-items: center;
    gap: 24px;
    margin-top: -10px;
  }
  .brand-dot {
    display: block;
    flex: none;
    width: 110px;
    height: 110px;
    border-radius: 50%;
    background: var(--navy);
  }
  .brand-name {
    font-size: 46px;
    font-weight: 500;
    letter-spacing: 2px;
    color: var(--navy);
    text-transform: uppercase;
    white-space: nowrap;
  }
  .back-brand {
    position: absolute;
    left: 95px;
    top: 140px;
    width: 260px;
    display: flex;
    flex-direction: column;
    align-items: center;
    gap: 20px;
  }
  .back-brand .brand-dot { width: 130px; height: 130px; background: var(--white); }
  .back-brand .brand-name { color: var(--white); font-size: 26px; letter-spacing: 1px; }
  .divider {
    position: absolute;
    left: 381px;
    top: 77px;
    width: 2px;
    height: 275px;
    background: var(--white);
  }
  .details {
    position: absolute;
    left: 413px;
    top: 84px;
  }
  .person-name { font-size: 29px; font-weight: 400; line-height: 1.1; }
  .person-role { font-size: 21px; font-weight: 700; margin-top: 4px; }
  .address { font-size: 23px; line-height: 32px; margin-top: 30px; }
  .contacts { list-style: none; margin-top: 30px; }
  .contacts li {
    display: flex;
    align-items: center;
    gap: 14px;
    font-size: 23px;
    line-height: 39px;
    white-space: nowrap;
  }
  .contacts svg { width: 16px; height: 16px; fill: var(--white); flex: none; }
</style>
</head>
<body>
  <section class="card card-front">
    <div class="brand">
      <span class="brand-dot"></span>
      <span class="brand-name">Ward Compass</span>
    </div>
  </section>

  <section class="card card-back">
    <div class="back-brand">
      <span class="brand-dot"></span>
      <span class="brand-name">Ward Compass</span>
    </div>
    <div class="divider"></div>
    <div class="details">
      <p class="person-name">Salma Derkaoui</p>
      <p class="person-role">CEO</p>
      <p class="address">14 Annakhil 3 H.R.B.<br>Rabat, Morocco</p>
      <ul class="contacts">
        <li>
          <svg viewBox="0 0 16 16" aria-hidden="true"><path d="M3.5 1.5l2.6 0.2 1 3.2-1.6 1.3a9 9 0 0 0 4.3 4.3l1.3-1.6 3.2 1v2.6c0 .9-.8 1.6-1.7 1.5C6.8 13.5 2.5 9.2 2 3.2 1.9 2.3 2.6 1.5 3.5 1.5z"/></svg>
          +90 612 348 2071
        </li>
        <li>
          <svg viewBox="0 0 16 16" aria-hidden="true"><path d="M1.5 4h13v1l-6.5 4.5L1.5 5z M1.5 6.6l6.5 4.5 6.5-4.5V12h-13z"/></svg>
          info@wardcompass-example.com
        </li>
        <li>
          <svg viewBox="0 0 16 16" aria-hidden="true"><path d="M8 1a7 7 0 1 0 0 14A7 7 0 0 0 8 1zm0 1.6c.8 0 1.7 1.5 2 3.9H6c.3-2.4 1.2-3.9 2-3.9zM2.7 7.5h2.1a13 13 0 0 1 0 1H2.7zm8.5 0h2.1v1h-2.1a13 13 0 0 0 0-1zM6 9.5h4c-.3 2.4-1.2 3.9-2 3.9s-1.7-1.5-2-3.9z"/></svg>
          www.wardcompass-example.com
        </li>
      </ul>
    </div>
  </section>
</body>
</html>
```